Stationary Design for Medical Distribution Company

We are a Medical Distribution Company based in Dar es salaam, Tanzania (East Africa). Our company was established in 1995 and we are a reputed and respected Pharmaceuticals and Medical Supplies company in the region.
We have just recently changed our company logo. A new company logo has just recently been selected through Pixel Harbor and we are now looking for stationary designs such as Business Cards, Letterheads, Envelopes, etc.. for our company.
We request you all to take a look at the attached new company logo and give us your best possible designs.
We would prefer to have a double sided business card. For letterheads, we are open to your ideas/designs.
We are looking forward for your designs!
Updates
Company details to be incorporated in designs:
Company Name: KOVEL PHARMACEUTICALS LIMITED
Company Address: Office # 42, Tumaini Works Ltd., Msasani Lane, Dar es salaam, Tanzania
Tel: +255 22 2917348 / 49, Fax: +255 22 2917350
Email: info@kovelmedix.example
Website: www.kovelmedix.example
Also should include Cell number +255 XXX XXX XXX
Name and Designation.....
Target Market(s)
Medical Sector
Industry/Entity Type
Medical
Look and feel

```html
<!DOCTYPE html>
<html lang="en">
<head>
<meta charset="utf-8">
<title>Kovel Pharmaceuticals Limited — Letterhead</title>
<link rel="stylesheet" href="https://fonts.googleapis.com/css2?family=Source+Sans+3:wght@400;500&display=swap">
<style>
  :root {
    --brand-red: #ed1c24;
    --ink: #231f20;
    --body-ink: #2b2b2b;
    --paper: #ffffff;
    --frame: #9a9a9a;
    --signature-blue: #1a8ed1;
  }
  * { margin: 0; padding: 0; box-sizing: border-box; }
  html, body { width: 849px; height: 1200px; overflow: hidden; background: var(--paper); }
  .letterhead {
    position: relative;
    width: 849px;
    height: 1200px;
    background: var(--paper);
    border: 1px solid var(--frame);
    font-family: "Source Sans 3", "Myriad Pro", sans-serif;
    color: var(--ink);
  }
  .brand {
    position: absolute;
    left: 499px;
    top: 56px;
    display: flex;
    align-items: center;
    gap: 11px;
  }
  .brand-square {
    width: 87px;
    height: 88px;
    border-radius: 9px;
    background: var(--brand-red);
  }
  .brand-name {
    font-size: 25px;
    line-height: 27px;
    font-weight: 400;
    color: var(--ink);
  }
  .letter-body {
    position: absolute;
    left: 160px;
    top: 274px;
    width: 548px;
    font-size: 10.4px;
    line-height: 16.7px;
    letter-spacing: 0.15px;
    color: var(--body-ink);
  }
  .letter-body p { text-indent: 50px; }
  .letter-body p + p { margin-top: 16px; }
  .sign-off {
    position: absolute;
    left: 160px;
    top: 677px;
    font-size: 12.5px;
    color: var(--body-ink);
  }
  .signature {
    position: absolute;
    left: 142px;
    top: 703px;
    width: 162px;
    height: 44px;
    background: linear-gradient(90deg, rgba(26,142,209,0.18), rgba(26,142,209,0.05));
    border-bottom: 1px solid var(--signature-blue);
  }
  .signatory {
    position: absolute;
    left: 160px;
    top: 760px;
    font-size: 12.5px;
    line-height: 18px;
    color: var(--body-ink);
  }
  .corner-block {
    position: absolute;
    left: 41px;
    top: 957px;
    width: 195px;
    height: 195px;
    border-radius: 14px;
    background: var(--brand-red);
  }
  .address {
    position: absolute;
    left: 400px;
    top: 1111px;
    display: flex;
    gap: 6px;
    font-size: 13px;
    line-height: 15.5px;
    color: var(--ink);
  }
  .contacts {
    position: absolute;
    left: 630px;
    top: 1086px;
    list-style: none;
    font-size: 13.5px;
    line-height: 18.7px;
    color: var(--ink);
  }
  .contacts li { display: flex; align-items: center; gap: 6px; }
  .icon { width: 14px; height: 14px; flex: none; }
  .address .icon { margin-top: 1px; }
</style>
</head>
<body>
<main class="letterhead">
  <header class="brand">
    <div class="brand-square"></div>
    <div class="brand-name">Kovel<br>Pharmaceuticals<br>Limited</div>
  </header>

  <section class="letter-body">
    <p>xx xxxxxx xxxxxxxx xxxxx xxxx xxxxx xxx xxxx xxxxxxxxxx xxxx xxx xxx xxxx xxxxx xxxx xxxxxx xxxxxxx xxxx xxx xxxxx xxxxxxx xxxxx xxxxxx xxx xxxx xxxx xxxx xxxxx xxxx xxxx xxxxxx xxxxx xxxxxxx xxxxxxxx xxxx xx xxxxxx xxxxxxxx xxxxx xxxx xxxxx xxx xxxx xxxxxxxxxx xxxx xxx xxx xxxx xxxxx xxxx xxxxxx xxxxxxx xxxx xxx xxxxx xxxxxxx xxxxx xxxxxx xxx xxxx xxxx xxxx xxxxx xxxx xxxx xxxxxx xxxxx xxxxxxx xxxxxxxx xxxx xx xxxxxx xxxxxxxx xxxxx xxxx xxxxx xxx xxxx xxxxxxxxxx xxxx xxx xxx xxxx xxxxx xxxx xxxxxx xxxxxxx xxxx xxx xxxxx xxxxxxx xxxxx xxxxxx xxx xxxx xxxx xxxx xxxxx xxxx xxxx xxxxxx xxxxx xxxxxxx xxxxxxxx xxxx xx xxxxxx xxxxxxxx xxxxx xxxx xxxxx xxx xxxx xxxxxxxxxx xxxx xxx xxx xxxx xxxxx xxxx xxxxxx xxxxxxx xxxx xxx xxxxx xxxxxxx xxxxx xxxxxx xxx xxxx xxxx xxxx xxxxx xxxx xxxx xxxxxx xxxxx xxxxxxx xxxxxxxx xxxx</p>
    <p>xx xxxxxx xxxxxxxx xxxxx xxxx xxxxx xxx xxxx xxxxxxxxxx xxxx xxx xxx xxxx xxxxx xxxx xxxxxx xxxxxxx xxxx xxx xxxxx xxxxxxx xxxxx xxxxxx xxx xxxx xxxx xxxx xxxxx xxxx xxxx xxxxxx xxxxx xxxxxxx xxxxxxxx xxxx xx xxxxxx xxxxxxxx xxxxx xxxx xxxxx xxx xxxx xxxxxxxxxx xxxx xxx xxx xxxx xxxxx xxxx xxxxxx xxxxxxx xxxx xxx xxxxx xxxxxxx xxxxx xxxxxx xxx xxxx xxxx xxxx xxxxx xxxx xxxx xxxxxx xxxxx xxxxxxx xxxxxxxx xxxx xx xxxxxx xxxxxxxx xxxxx xxxx xxxxx xxx xxxx xxxxxxxxxx xxxx xxx xxx xxxx xxxxx xxxx xxxxxx xxxxxxx xxxx xxx xxxxx xxxxxxx xxxxx xxxxxx xxx xxxx xxxx xxxx xxxxx xxxx xxxx xxxxxx xxxxx xxxxxxx xxxxxxxx xxxx</p>
  </section>

  <p class="sign-off">Yours</p>
  <div class="signature" role="img" aria-label="Handwritten signature in blue ink"></div>
  <p class="signatory">dkkdksfslfsfjs<br>slssl</p>

  <div class="corner-block"></div>

  <address class="address" style="font-style:normal">
    <svg class="icon" viewBox="0 0 14 14" aria-hidden="true">
      <circle cx="7" cy="7" r="7" fill="var(--brand-red)"/>
      <path d="M3 7.2 7 3.6l4 3.6M4.4 6.4v4h5.2v-4" fill="none" stroke="#fff" stroke-width="1.3"/>
    </svg>
    <span>42, Tumaini Works Ltd.,<br>Msasani Lane, Dar es salaam,<br>Tanzania</span>
  </address>

  <ul class="contacts">
    <li>
      <svg class="icon" viewBox="0 0 14 14" aria-hidden="true">
        <rect width="14" height="14" rx="3" fill="var(--brand-red)"/>
        <rect x="4.5" y="2.5" width="5" height="9" rx="1" fill="none" stroke="#fff" stroke-width="1.2"/>
      </svg>
      <span>+255 22 2917348 / 49</span>
    </li>
    <li>
      <svg class="icon" viewBox="0 0 14 14" aria-hidden="true">
        <rect width="14" height="14" rx="3" fill="var(--brand-red)"/>
        <path d="M3 6h8v5H3zM5 6V3h4v3" fill="none" stroke="#fff" stroke-width="1.2"/>
      </svg>
      <span>+255 22 2917350</span>
    </li>
    <li>
      <svg class="icon" viewBox="0 0 14 14" aria-hidden="true">
        <rect width="14" height="14" rx="3" fill="var(--brand-red)"/>
        <path d="M2.5 4h9v6.5h-9zM2.5 4 7 8l4.5-4" fill="none" stroke="#fff" stroke-width="1.1"/>
      </svg>
      <span>info@kovelmedix.example</span>
    </li>
    <li>
      <svg class="icon" viewBox="0 0 14 14" aria-hidden="true">
        <circle cx="7" cy="7" r="7" fill="var(--brand-red)"/>
        <circle cx="7" cy="7" r="4.2" fill="none" stroke="#fff" stroke-width="1"/>
        <path d="M2.8 7h8.4M7 2.8c-2 2.6-2 5.8 0 8.4M7 2.8c2 2.6 2 5.8 0 8.4" fill="none" stroke="#fff" stroke-width="0.9"/>
      </svg>
      <span>www.kovelmedix.example</span>
    </li>
  </ul>
</main>
</body>
</html>
```